Personal Brand Business Card

I am looking for a design that I will use as my personal brand that conveys class (think 1920s gentlemen) and is timeless. I will be putting this on a pearl white, letter pressed, cotton business card.  I’m thinking maybe something with my initials on the front they will flip over for the rest of my information.  But don’t let that limit you.
The information I will have on the back of the business card will be my name, email, and phone number.
Some of the attributes that best describe me are: loyal, dependable, creative, risk taker, open minded, competitive, and empathetic.  I can adapt to my environment quickly and can get along with anyone.  I get excited by figuring out the way things work and finding solutions to problems.

Industry/Entity Type
Business

```html
<!DOCTYPE html>
<html lang="en">
<head>
<meta charset="utf-8">
<title>Dean Hallworth — Business Card</title>
<link rel="stylesheet" href="https://fonts.googleapis.com/css2?family=Questrial&display=swap">
<style>
  :root {
    --paper: #ffffff;
    --ink: #000000;
    --muted: #555555;
    --faint: #d6d6d6;
    --stage: #ffffff;
    --edge: #e4e4e4;
  }
  * { box-sizing: border-box; margin: 0; padding: 0; }
  html, body {
    width: 1200px;
    height: 1193px;
    overflow: hidden;
    background: var(--stage);
    font-family: "Questrial", Arial, sans-serif;
  }
  .stage { position: relative; width: 1200px; height: 1193px; }

  .card {
    position: absolute;
    width: 722px;
    height: 412px;
    background: var(--paper);
    outline: 1px solid var(--edge);
    overflow: hidden;
  }
  .card--details { left: 45px; top: 45px; }
  .card--monogram { left: 358px; top: 524px; }

  .corner-mark { position: absolute; }
  .card--details .corner-mark { left: 19px; top: 19px; }
  .card--monogram .corner-mark { right: 14px; bottom: 15px; }

  .identity {
    position: absolute;
    left: 0; right: 0;
    top: 42px;
    text-align: center;
    color: var(--ink);
  }
  .identity__initials {
    font-size: 36px;
    letter-spacing: 2px;
    line-height: 1;
  }
  .identity__name {
    margin-top: 12px;
    font-size: 37px;
    line-height: 1;
  }
  .identity__role {
    margin-top: 12px;
    font-size: 24px;
    letter-spacing: 1px;
    color: var(--muted);
    line-height: 1;
  }

  .contact-band {
    position: absolute;
    left: 0; bottom: 0;
    width: 109px;
    height: 166px;
    background: var(--ink);
  }
  .contact-list {
    position: absolute;
    left: 0; top: 311px;
    list-style: none;
  }
  .contact-list__item {
    position: relative;
    height: 54px;
    display: flex;
    align-items: center;
  }
  .contact-list__icon {
    width: 109px;
    display: flex;
    justify-content: center;
  }
  .contact-list__text {
    margin-left: 13px;
    font-size: 22px;
    color: var(--ink);
  }

  .monogram-watermark {
    position: absolute;
    left: 0; right: 0;
    top: 8px;
    text-align: center;
    font-size: 420px;
    line-height: 1;
    color: var(--faint);
    letter-spacing: -10px;
  }
  .monogram-initials {
    position: absolute;
    left: 0; right: 0;
    top: 110px;
    text-align: center;
    font-size: 170px;
    line-height: 1;
    color: var(--ink);
    letter-spacing: 6px;
  }
</style>
</head>
<body>
<main class="stage">

  <section class="card card--details" aria-label="Card side with contact details">
    <svg class="corner-mark" width="99" height="99" viewBox="0 0 99 99" aria-hidden="true">
      <path d="M0 0H99V52H49V99H0Z" fill="var(--ink)"/>
    </svg>

    <header class="identity">
      <div class="identity__initials">DH</div>
      <h1 class="identity__name" style="font-weight:400">Dean Hallworth</h1>
      <p class="identity__role">CONSULTANT</p>
    </header>

    <div class="contact-band"></div>
    <ul class="contact-list">
      <li class="contact-list__item">
        <span class="contact-list__icon">
          <svg width="44" height="28" viewBox="0 0 44 28" aria-hidden="true">
            <rect x="1.5" y="1.5" width="41" height="25" fill="none" stroke="#fff" stroke-width="2.5"/>
            <path d="M2 2L22 17L42 2M2 26L17 13M42 26L27 13" fill="none" stroke="#fff" stroke-width="2.5"/>
          </svg>
        </span>
        <span class="contact-list__text">dean.hallworth@mailbox.net</span>
      </li>
      <li class="contact-list__item">
        <span class="contact-list__icon">
          <svg width="40" height="40" viewBox="0 0 24 24" aria-hidden="true">
            <path d="M6.6 2.5l3 3.6-2 2.3c1.3 2.9 3.6 5.3 6.6 6.8l2.3-2 3.6 3-1.7 3c-.4.6-1.1.9-1.8.7C9.6 18.5 5.4 14.3 3.6 7.4c-.2-.7.1-1.4.7-1.8z"
                  fill="none" stroke="#fff" stroke-width="1.3" stroke-linejoin="round"/>
          </svg>
        </span>
        <span class="contact-list__text">555-014-2287</span>
      </li>
    </ul>
  </section>

  <section class="card card--monogram" aria-label="Card side with initials">
    <div class="monogram-watermark" aria-hidden="true">DH</div>
    <div class="monogram-initials">DH</div>
    <svg class="corner-mark" width="99" height="101" viewBox="0 0 99 101" aria-hidden="true">
      <path d="M49 0H99V101H0V50H49Z" fill="var(--ink)"/>
    </svg>
  </section>

</main>
</body>
</html>
```